A new updated business card. A good first impression for new customers to our business.

I need something unique. I will attached a picture of our old rubbish cards, and also our current Logo ( I think this needs an update if you have any ideas, its very basic and budget)The best way you will get to see my business is checking our Facebook page, I don't really know what else to say, but anything you want to know, ask away.www.facebook.com/tmwjetwashing/

Target Market(s)

Home owners

Industry/Entity Type

Business

Contact Information for Business Card

T&M's Surface Washing & Paving Coating
Lina 0481 226 579 lina@tmwjetwashing.com
Dalton 0452 318 960 dalton@tmwjetwashing.com

FB: www.facebook.com/tmwjetwashing/
Website: www.tmwjetwashing.net (This is pretty rubbish- we don't really use it)

100% customer satisfaction guaranteed

All aspects of Hi-Pressure Cleaning
Sealing & Re-Sealing
Roof Cleaning
Colour sealing
Decorative coatings

Free no obligation quotes

Requirements
Must have
• NO OBLIGATION FREE quotes
• 100% Customer satisfaction guaranteed
• Can you please add both names, contact details and email address on one card.
• Dalton 0452 318 960
• dalton@tmwjetwashing.com
• Lina 0481 226 579
• lina@tmwjetwashing.com
• Please change the services:
• Hot/Cold Hi-Pressure Cleaning
• Sealing & Re-Sealing
• Roof Cleaning
• Colour Sealing
• Decorative Coatings
• Concrete Honing
• Thanks
Nice to have
• Something a bit different, something eye catching.l

```html
<!DOCTYPE html>
<html lang="en">
<head>
<meta charset="utf-8">
<title>T&amp;M's Surface Washing &amp; Paving Coating – Business Card</title>
<link href="https://fonts.googleapis.com/css2?family=Open+Sans:wght@400;600;700&display=swap" rel="stylesheet">
<style>
  :root {
    --backdrop: #e9e6e3;
    --card-white: #ffffff;
    --brand-red: #f80008;
    --ink-dark: #3a3a3a;
    --ink-light: #ffffff;
  }
  * { box-sizing: border-box; margin: 0; padding: 0; }
  html, body {
    width: 1200px; height: 900px; overflow: hidden;
    background: var(--backdrop);
    font-family: "Open Sans", Arial, sans-serif;
  }
  .canvas { position: relative; width: 1200px; height: 900px; }

  .card {
    position: absolute;
    background: var(--card-white);
    overflow: hidden;
    box-shadow: 0 6px 18px rgba(0,0,0,0.18);
  }
  .card--front { left: 77px; top: 35px; width: 588px; height: 362px; }
  .card--back  { left: 388px; top: 506px; width: 566px; height: 351px; }

  /* Front */
  .brand {
    position: absolute; left: 0; top: 0; width: 100%; height: 207px;
    display: flex; flex-direction: column; align-items: center; justify-content: center;
    gap: 10px;
  }
  .brand__mark {
    width: 22px; height: 22px; border-radius: 50%;
    background: var(--ink-dark);
  }
  .brand__name {
    color: var(--ink-dark);
    font-weight: 700; font-size: 23px; line-height: 1.25;
    text-align: center; letter-spacing: 0.5px;
  }
  .contact-band {
    position: absolute; left: 0; top: 207px; width: 100%; height: 155px;
    background: var(--brand-red);
    color: var(--ink-light);
  }
  .contact {
    position: absolute; top: 12px;
    display: flex; flex-direction: column;
    font-size: 15px; line-height: 1;
  }
  .contact--left  { right: 314px; align-items: flex-end; }
  .contact--right { left: 311px; align-items: flex-start; }
  .contact__name { font-weight: 600; font-size: 21px; margin-bottom: 10px; }
  .contact__row { display: flex; align-items: center; gap: 8px; height: 26px; }
  .contact__row--social { margin-top: 6px; }
  .icon { width: 12px; height: 12px; fill: var(--ink-light); flex: none; }
  .social-square { width: 10px; height: 10px; background: var(--ink-light); flex: none; }

  /* Back */
  .promise-band {
    position: absolute; left: 0; top: 110px; width: 100%; height: 130px;
    background: var(--brand-red); color: var(--ink-light);
    display: flex; flex-direction: column; align-items: center;
    padding-top: 14px;
  }
  .promise__title { font-weight: 600; font-size: 19px; margin-bottom: 14px; }
  .promise__services { font-weight: 600; font-size: 14px; line-height: 27px; text-align: center; }
  .quote-offer {
    position: absolute; left: 0; top: 240px; width: 100%; height: 111px;
    display: flex; align-items: center; justify-content: center;
    color: var(--brand-red); font-weight: 700; font-size: 19px;
  }
</style>
</head>
<body>
<div class="canvas">

  <section class="card card--front">
    <div class="brand">
      <span class="brand__mark"></span>
      <div class="brand__name">T&amp;M's Surface Washing<br>&amp; Paving Coating</div>
    </div>

    <div class="contact-band">
      <div class="contact contact--left">
        <div class="contact__name">Lina</div>
        <div class="contact__row">0481 226 579
          <svg class="icon" viewBox="0 0 24 24"><path d="M6.6 10.8a15.5 15.5 0 0 0 6.6 6.6l2.2-2.2c.3-.3.7-.4 1-.2 1.1.4 2.3.6 3.6.6.6 0 1 .4 1 1V20c0 .6-.4 1-1 1A17 17 0 0 1 3 4c0-.6.4-1 1-1h3.5c.6 0 1 .4 1 1 0 1.3.2 2.5.6 3.6.1.3 0 .7-.2 1z"/></svg>
        </div>
        <div class="contact__row">lina@tmwjetwashing.com
          <svg class="icon" viewBox="0 0 24 24"><path d="M2 5h20v14H2z M2 5l10 7 10-7" fill="none" stroke="#fff" stroke-width="2.4"/></svg>
        </div>
        <div class="contact__row contact__row--social">tmwjetwashing
          <span class="social-square"></span>
        </div>
      </div>

      <div class="contact contact--right">
        <div class="contact__name">Dalton</div>
        <div class="contact__row">
          <svg class="icon" viewBox="0 0 24 24"><path d="M6.6 10.8a15.5 15.5 0 0 0 6.6 6.6l2.2-2.2c.3-.3.7-.4 1-.2 1.1.4 2.3.6 3.6.6.6 0 1 .4 1 1V20c0 .6-.4 1-1 1A17 17 0 0 1 3 4c0-.6.4-1 1-1h3.5c.6 0 1 .4 1 1 0 1.3.2 2.5.6 3.6.1.3 0 .7-.2 1z"/></svg>
          0452 318 960</div>
        <div class="contact__row">
          <svg class="icon" viewBox="0 0 24 24"><path d="M2 5h20v14H2z M2 5l10 7 10-7" fill="none" stroke="#fff" stroke-width="2.4"/></svg>
          dalton@tmwjetwashing.com</div>
        <div class="contact__row contact__row--social">
          <svg class="icon" viewBox="0 0 24 24"><circle cx="12" cy="12" r="10" fill="none" stroke="#fff" stroke-width="2.4"/><path d="M2 12h20M12 2c3 3 3 17 0 20M12 2c-3 3-3 17 0 20" fill="none" stroke="#fff" stroke-width="2"/></svg>
          www.tmwjetwashing.net</div>
      </div>
    </div>
  </section>

  <section class="card card--back">
    <div class="promise-band">
      <div class="promise__title">100% customer satisfaction guaranteed</div>
      <div class="promise__services">
        Hot/Cold Hi-Pressure Cleaning | Sealing &amp; Re-Sealing | Roof Cleaning<br>
        Colour Sealing | Decorative Coatings | Concrete Honing
      </div>
    </div>
    <div class="quote-offer">No obligation FREE quotes</div>
  </section>

</div>
</body>
</html>
```